Bifold for voip company

Bifold for cloud voip company

Target Market(s)

Business owners

Industry/Entity Type

Software Developer

Colors

Designer to choose colors to be used in the design.

Requirements
Must have
• Modern clean design,
• will provide content to design winner

```html
<!DOCTYPE html>
<html lang="en">
<head>
<meta charset="utf-8">
<title>Nuvolink Bifold Cover</title>
<link rel="stylesheet" href="https://fonts.googleapis.com/css2?family=Montserrat:wght@300;400;500;700;800&display=swap">
<style>
  :root {
    --backdrop: #2b2b2b;
    --paper: #ffffff;
    --paper-shade: #eeeef0;
    --ink: #2f2f35;
    --ink-soft: #6b6b73;
    --purple: #4b2a7e;
    --teal: #35bfd6;
    --photo-dark: #1f2a36;
    --photo-mid: #4a5866;
    --photo-light: #7f8e9a;
  }
  * { margin: 0; padding: 0; box-sizing: border-box; }
  html, body {
    width: 1200px; height: 790px; overflow: hidden;
    background: var(--backdrop);
    font-family: "Montserrat", sans-serif;
  }
  .cover {
    position: absolute; left: 340px; top: 27px;
    width: 520px; height: 736px;
    background: var(--paper);
    overflow: hidden;
  }
  .cover-shapes { position: absolute; inset: 0; }
  .brand {
    position: absolute; top: 44px; right: 44px;
    display: flex; align-items: center; gap: 10px;
  }
  .brand-mark { width: 16px; height: 16px; background: var(--purple); }
  .brand-name {
    font-size: 30px; font-weight: 500; letter-spacing: 3px;
    color: var(--ink-soft); text-transform: uppercase;
  }
  .headline {
    position: absolute; right: 30px; top: 420px;
    text-align: right; color: var(--purple);
  }
  .headline-clouds { display: block; margin-left: auto; margin-right: 10px; }
  .headline-lead {
    display: block; font-size: 30px; font-weight: 300;
    color: var(--ink); letter-spacing: 1px; margin-top: 2px;
  }
  .headline-main {
    display: block; font-size: 54px; font-weight: 800; line-height: 1;
  }
  .headline-sub {
    display: flex; align-items: center; justify-content: flex-end; gap: 12px;
    font-size: 38px; font-weight: 800;
    line-height: 1.15; letter-spacing: 0.5px;
  }
  .tagline {
    position: absolute; right: 30px; top: 596px;
    text-align: right; font-size: 19px; font-weight: 400;
    color: var(--ink); line-height: 1.35;
  }
  .tagline strong { color: var(--teal); font-weight: 800; }
  .website {
    position: absolute; left: 30px; bottom: 30px;
    display: flex; align-items: center; gap: 8px;
    font-size: 17px; color: var(--ink);
  }
  .website strong { color: var(--purple); font-weight: 800; }
</style>
</head>
<body>
  <article class="cover">
    <svg class="cover-shapes" width="520" height="736" viewBox="0 0 520 736">
      <defs>
        <linearGradient id="photoTone" x1="0" y1="0" x2="1" y2="1">
          <stop offset="0" stop-color="var(--photo-light)"/>
          <stop offset="0.45" stop-color="var(--photo-mid)"/>
          <stop offset="1" stop-color="var(--photo-dark)"/>
        </linearGradient>
      </defs>
      <path class="corner-shade" d="M0 0 L230 0 Q160 40 0 110 Z" fill="var(--paper-shade)"/>
      <path class="corner-shade" d="M520 520 L520 736 L330 736 Z" fill="var(--paper-shade)"/>
      <path class="hero-photo" role="img"
            aria-label="Photo of a business person holding a tablet with a glowing cloud network diagram"
            d="M0 135 L240 70 Q275 62 298 88 L420 235 Q438 258 420 282 L265 488 Q245 512 215 512 L0 512 Z"
            fill="url(#photoTone)"/>
      <line class="tagline-rule" x1="205" y1="672" x2="492" y2="658" stroke="var(--purple)" stroke-width="1.2"/>
      <circle cx="205" cy="672" r="3" fill="var(--purple)"/>
    </svg>

    <div class="brand">
      <span class="brand-mark"></span>
      <span class="brand-name">Nuvolink</span>
    </div>

    <h1 class="headline">
      <svg class="headline-clouds" width="140" height="36" viewBox="0 0 140 36" aria-hidden="true">
        <path d="M6 32 Q0 32 2 24 Q5 18 12 20 Q16 10 28 13 Q34 6 44 14 Q54 14 54 24 Q56 32 48 32 Z"
              fill="none" stroke="var(--teal)" stroke-width="2.5"/>
        <path d="M64 30 Q56 30 58 22 Q62 14 72 17 Q78 4 94 8 Q104 2 114 12 Q128 12 130 22 Q132 30 122 30 Z"
              fill="none" stroke="var(--purple)" stroke-width="2.5"/>
      </svg>
      <span class="headline-lead">REDEFINING</span>
      <span class="headline-main">CLOUD</span>
      <span class="headline-sub">COMMUNICATION</span>
    </h1>

    <p class="tagline">Work from the <strong>OFFICE, HOME</strong><br>or on the road.</p>

    <p class="website">
      <svg width="16" height="16" viewBox="0 0 16 16" aria-hidden="true">
        <g fill="none" stroke="var(--teal)" stroke-width="1.2">
          <circle cx="8" cy="8" r="6.5"/>
          <ellipse cx="8" cy="8" rx="3" ry="6.5"/>
          <line x1="1.5" y1="8" x2="14.5" y2="8"/>
        </g>
      </svg>
      <span>www.<strong>nuvolink</strong>.com</span>
    </p>
  </article>
</body>
</html>
```